Geschäftspapiere für Hundebetreuung
Zielgruppe
Mein Unternehmen richtet sich an Hundehalter, die freudig mit ihrem Hund arbeiten oder trainieren wollen oder eine positiv arbeitende Hundebetreuung oder Gassi-Gänger suchen. Hierbei liegt der Fokus auf Emotionen des Hundes, Emotionen des Hundehalters, Körpersprache und kleinschrittiges Training. Gemeinsames freudiges Training schafft Vertrauen und Bindung und ermöglicht Hund und Halter Freiraum. Ziel des Angebotes ist es, dass Hundehalter Verständnis für die Emotionen und Interessen des Hundes zu entwickeln und das für sich zu nutzen lernen, dem Hund das geben, was er in der jeweiligen Situation braucht und das ganze auf wissenschaftlich fundierter Basis.
Aufgabenstellung
Das Logo muss enthalten sein, ansonsten sind der Kreativität keine Grenzen gesetzt :)
Es sollte nur von Rechnung, über Angebot für alles nutzbar sein.
Das Unternehmen ist ein Einzelunternehmen, sprich der Firmenname ist mein eigener Name 'Doris Lamprecht' und Pfotenbande nur Website und Marke.

```html
<!DOCTYPE html>
<html lang="de">
<head>
<meta charset="utf-8">
<title>Pfotenbande – Briefbogen</title>
<link href="https://fonts.googleapis.com/css2?family=Poppins:wght@300;400;500;600&display=swap" rel="stylesheet">
<style>
  :root {
    --green: #8bb92a;
    --slate: #44565d;
    --paper: #ffffff;
    --footer-grey: #ebebeb;
    --fold: #d6d6d6;
  }
  * { margin: 0; padding: 0; box-sizing: border-box; }
  html, body { width: 848px; height: 1200px; overflow: hidden; background: var(--paper); }
  body { font-family: "Poppins", sans-serif; color: var(--slate); position: relative; font-weight: 300; }
  .backdrop { position: absolute; inset: 0; }
  .web-address { position: absolute; left: 89px; top: 42px; font-size: 17px; font-weight: 500; color: var(--slate); letter-spacing: .2px; }
  .brand-block { position: absolute; left: 535px; top: 64px; width: 232px; }
  .brand-scene { display: block; width: 232px; height: 112px; border-radius: 4px;
    background: linear-gradient(180deg, #f3f5f1 0%, #c7ccc8 55%, #8bb92a 100%); }
  .brand-name { display: block; text-align: center; margin-top: 8px; font-size: 34px; font-weight: 500; color: var(--slate); line-height: 1; }
  .sender-line { position: absolute; left: 89px; top: 214px; font-size: 11px; color: var(--green); font-weight: 400; white-space: nowrap; }
  .sender-line .sender-brand { color: var(--slate); font-weight: 400; }
  .sender-line .dot { color: var(--slate); margin: 0 5px; }
  .recipient { position: absolute; left: 89px; top: 246px; font-size: 14.5px; line-height: 20px; font-weight: 400; }
  .recipient strong { font-weight: 600; }
  .fold-mark { position: absolute; left: 0; width: 36px; height: 1px; background: var(--fold); }
  .letter-date { position: absolute; right: 89px; top: 450px; font-size: 14.5px; font-weight: 400; }
  .letter-body { position: absolute; left: 89px; top: 522px; width: 670px; }
  .subject { font-size: 18.5px; font-weight: 600; margin-bottom: 14px; }
  .letter-body p { font-size: 14.5px; line-height: 20px; text-align: justify; hyphens: auto; margin-bottom: 20px; font-weight: 400; }
  .letter-body p.closing { text-align: left; }
  .footer-dog { position: absolute; left: 658px; top: 1034px; width: 78px; height: 60px; border-radius: 30px 30px 12px 12px; background: var(--slate); }
  .footer-dot { position: absolute; left: 745px; top: 1081px; width: 13px; height: 13px; border-radius: 50%; background: var(--green); }
  .footer-brand { position: absolute; left: 89px; top: 1106px; font-size: 23px; font-weight: 500; color: var(--slate); }
  .footer-col { position: absolute; top: 1109px; font-size: 11px; line-height: 16.5px; font-weight: 400; }
  .footer-col strong { font-weight: 600; }
  .footer-address { left: 243px; }
  .footer-contact { left: 390px; }
  .footer-contact .row { display: flex; align-items: center; gap: 8px; }
  .footer-contact svg { width: 9px; height: 9px; fill: var(--green); flex: none; }
  .footer-bank { left: 586px; }
  .footer-bank .label { color: var(--green); font-weight: 600; }
  .footer-bank .key { display: inline-block; width: 34px; font-weight: 600; }
</style>
</head>
<body>
  <svg class="backdrop" width="848" height="1200" viewBox="0 0 848 1200" aria-hidden="true">
    <path d="M0 0 H848 V78 C790 56 760 56 700 62 C560 78 420 118 200 110 C110 106 40 96 0 82 Z" fill="var(--green)"/>
    <path d="M742 67 C790 72 825 88 848 112 V100 C820 80 790 70 742 67 Z" fill="var(--slate)"/>
    <path d="M0 1086 C140 1080 300 1060 460 1068 C600 1075 720 1100 848 1138 V1200 H0 Z" fill="var(--footer-grey)"/>
    <path d="M0 1022 C30 1045 70 1062 112 1070 C70 1068 30 1058 0 1048 Z" fill="var(--green)"/>
  </svg>

  <div class="web-address">www.pfotenbande.de</div>

  <div class="brand-block">
    <span class="brand-scene" role="img" aria-label="Illustration: Berglandschaft mit Tannen, eine Frau und ein Hund im Schattenriss"></span>
    <span class="brand-name">Pfotenbande</span>
  </div>

  <div class="sender-line"><span class="sender-brand">Pfotenbande</span><span class="dot">•</span>Musterstraße 1<span class="dot">•</span>12345 Musterstadt</div>

  <address class="recipient" style="font-style:normal">
    <strong>Musterfirma GmbH</strong><br>
    Max Mustermann<br>
    Musterstraße 123<br>
    12345 Musterstadt
  </address>

  <div class="fold-mark" style="top:424px"></div>
  <div class="fold-mark" style="top:808px"></div>

  <div class="letter-date">Musterstadt, 01.01.2022</div>

  <main class="letter-body">
    <h1 class="subject">Betreff: Endam, omni dolor sam asperro que eos es</h1>
    <p>Uptassi quo volupta dit aliberis dolutas pelestrum sendi remquam repellent as autemodis eturit faciae illorrorest, omnimilit, qui ut endiscillam quid que sandero eiunt eror rest quam, temporunt officip sandam imi, sit acepudandis cor si cus, cum adios nonsedipsa consequ aesedit rem. Minus, inis am nos nossus vendaer uptiis mi, quiae con possi natis etur, simagna tionsed ullo venditia id ut auda isqui occus.</p>
    <p>Porest ma dolupta et accusdamusam sunt omnimil laborestia con commolum fugiaerio et iunt labor sequi velite et desciis sero modis nullandes del molliquo iliquis et eaquaspere sitiis es elenis dolendant exceperes es elenis dolendant exceperes es everest ibeatentia voloris ad millate il inctur? eatentia voloris ad millate il inctur? Qui vent venti ilibus.</p>
    <p>Excessi vel maximpo rporepe poreperum qui omniste eatenda quo es et omniaepudam, qui debissinci ullabor eptatempor modiorrum quos sus dolum ad quos et quias alissi debis nullore strunt porerum, sit vole.</p>
    <p class="closing">Herzlichst,<br>Erika Mustermann</p>
  </main>

  <div class="footer-dog" role="img" aria-label="Illustration: laufender Hund im Schattenriss"></div>
  <div class="footer-dot"></div>

  <div class="footer-brand">Pfotenbande</div>

  <div class="footer-col footer-address">
    Musterstraße 1<br>
    12345 Musterstadt<br>
    <strong>Geschäftsführung:</strong><br>
    Erika Mustermann
  </div>

  <div class="footer-col footer-contact">
    <div class="row"><svg viewBox="0 0 10 10"><path d="M2 0.5 L3.6 2.6 L2.8 3.6 C3.4 5 4.8 6.4 6.2 7 L7.2 6.2 L9.4 7.8 L8.4 9.4 C4.5 9.4 0.6 5.5 0.6 1.6 Z"/></svg>+49 (0)1234 – 123 456 78</div>
    <div class="row"><svg viewBox="0 0 10 10"><rect x="2.5" y="0.5" width="5" height="9" rx="1" fill="none" stroke="var(--green)" stroke-width="1"/></svg>+49 (0)1234 – 123 456 78</div>
    <div class="row"><svg viewBox="0 0 10 10"><path d="M0.5 2 H9.5 V8 H0.5 Z M0.5 2 L5 5.5 L9.5 2" fill="var(--green)" stroke="#fff" stroke-width="0.6"/></svg>kontakt@pfotenbande.de</div>
    <div class="row"><strong>www.pfotenbande.de</strong></div>
  </div>

  <div class="footer-col footer-bank">
    <span class="label">Bankverbindung</span><br>
    <strong>Musterbank AG</strong><br>
    <span class="key">IBAN:</span>DE12 1234 1234 1234 1234 00<br>
    <span class="key">BIC:</span>ABCDEFGHJK
  </div>
</body>
</html>
```